Resume redesign

I'm a researcher who works with web design companies. I'm updating my resume but want more than the standard black and white wall of text. The content is updated, what I need is a design to make it readable, or in the words of my friend the hiring manager 'it needs to have high scan value'. It has to strike some balance between professionalism and readability.

There are two versions of my resume attached. I'm willing to cut some information if needed or reword things to simplify them. It would be great if it could be cut down to 2 pages, although this may require eliminating the publications section (which is fine).

```html
<!DOCTYPE html>
<html lang="en">
<head>
<meta charset="utf-8">
<title>Daniel Reyes – Research Consultant</title>
<link href="https://fonts.googleapis.com/css2?family=Arimo:ital,wght@0,400;0,700;1,400&display=swap" rel="stylesheet">
<style>
  :root {
    --blue: #2a9ad8;
    --ink: #1b4f78;
    --ink-dark: #2b2b2b;
    --paper: #ffffff;
  }
  * { margin: 0; padding: 0; box-sizing: border-box; }
  html, body { width: 849px; height: 1200px; overflow: hidden; background: var(--paper); }
  body { font-family: "Arimo", Arial, sans-serif; }
  .resume { position: relative; width: 849px; height: 1200px; background: var(--paper); overflow: hidden; }

  .name { position: absolute; left: 34px; top: 10px; width: 570px; white-space: nowrap; font-size: 46px; font-weight: 700; color: var(--blue); letter-spacing: -0.5px; line-height: 1.1; }
  .title { position: absolute; left: 34px; top: 66px; font-size: 21px; color: var(--ink-dark); }
  .header-block { position: absolute; left: 620px; top: 0; width: 229px; height: 88px; background: var(--blue); }
  .header-rule { position: absolute; left: 14px; top: 106px; width: 582px; height: 5px; background: var(--blue); }

  .section-head { position: absolute; left: 14px; width: 582px; height: 28px; background: var(--paper); border-left: 9px solid var(--blue); padding-left: 14px; font-size: 20px; font-weight: 700; color: var(--ink-dark); line-height: 28px; }
  .band { position: absolute; left: 14px; width: 582px; background: var(--blue); color: var(--paper); overflow: hidden; }

  .profile-head { top: 118px; }
  .profile { top: 150px; height: 160px; padding: 12px 18px 0 20px; font-size: 12.3px; line-height: 17px; }

  .education-head { top: 314px; }
  .education { top: 344px; height: 234px; padding: 10px 20px; display: grid; grid-template-columns: 1fr 1fr; row-gap: 20px; font-size: 13.4px; line-height: 25px; }
  .edu-label { font-weight: 700; }
  .edu-school { font-style: italic; }

  .experience-head { top: 584px; }
  .experience { position: absolute; left: 34px; top: 628px; width: 550px; color: var(--ink); font-size: 12.8px; line-height: 18.6px; }
  .job { margin-bottom: 12px; }
  .job-org { font-weight: 700; font-size: 13.4px; }
  .job-role { font-style: italic; font-weight: 400; margin-left: 12px; }
  .job-role.small { font-size: 9.5px; margin-left: 6px; }
  .job-dates { font-style: italic; font-size: 11.5px; }
  .sub { font-style: italic; }

  .side-bar { position: absolute; left: 620px; width: 229px; background: var(--blue); color: var(--paper); font-size: 20px; font-weight: 700; padding-left: 14px; }
  .contact-head { top: 150px; height: 47px; line-height: 47px; }
  .skills-head { top: 421px; height: 42px; line-height: 42px; }
  .contact { position: absolute; left: 632px; top: 236px; font-size: 13.6px; line-height: 19px; color: var(--ink-dark); font-style: normal; }
  .contact p { margin-bottom: 24px; }
  .skills { position: absolute; left: 632px; top: 472px; list-style: none; font-size: 14px; line-height: 20px; color: var(--ink-dark); }
  .side-foot { position: absolute; left: 620px; top: 912px; width: 229px; height: 288px; background: var(--blue); }
</style>
</head>
<body>
<main class="resume">
  <h1 class="name">Daniel Reyes, PhD, MBA</h1>
  <p class="title">Research Consultant</p>
  <div class="header-block"></div>
  <div class="header-rule"></div>

  <h2 class="section-head profile-head">Profile</h2>
  <section class="band profile">
    Forward-thinking and dynamic Senior Research Consultant with experience leading targeted research strategies and data collection initiatives to drive project success and reduce spending. Expert communicator who leverages strong research acumen to obtain key customer insight, collect and analyze data; and provide accurate primary and secondary findings to deliver value-enhancing recommendations across major, multimillion dollar projects with organizations including Telvana, MediCore, Compuline, and Harbor Bank. Expertise in developing customized and detailed research solutions to fit the scope of a range of projects and ensure accurate and profitable results.
  </section>

  <h2 class="section-head education-head">Education</h2>
  <section class="band education">
    <div class="edu-item">
      <div class="edu-label">Graduate Studies</div>
      <div class="edu-school">Coastal State University</div>
      <div>Ph.D. in Anthropology,<br>Research Methodology</div>
    </div>
    <div class="edu-item">
      <div class="edu-label">Graduate Studies</div>
      <div class="edu-school">Delta Valley University</div>
      <div>Master of Business<br>Administration</div>
    </div>
    <div class="edu-item">
      <div class="edu-label">Graduate Studies</div>
      <div class="edu-school">Prairie State University</div>
      <div>Bachelor of Arts in<br>Anthropology</div>
    </div>
    <div class="edu-item">
      <div class="edu-label">Certificate</div>
      <div>National Science Alliance<br>Summer Institute for Research<br>Design in Cultural Anthropology</div>
    </div>
  </section>

  <h2 class="section-head experience-head">Experiences</h2>
  <section class="experience">
    <article class="job">
      <div class="job-org">Brightpath Research, LLC.<span class="job-role">Principle Researcher</span></div>
      <div class="job-dates">2007 - Present</div>
      <p>Design and implement effective, top-tier research design for a range of projects and industries. Directly interface with clients to communicate research processes and findings while collecting and analyzing appropriate types of data to recommend easily understood, actionable, and highly customized solutions and results.</p>
    </article>
    <article class="job">
      <div class="job-org">Northwave Digital.<span class="job-role">Contracted Senior Researcher</span></div>
      <div class="job-dates">2008 - 2013</div>
      <p>Drove and developed key primary and secondary research to create practical findings and compose detailed research plans for a range of multimillion dollar digital projects. Collected and analyzed data for both internal and external clients. Collaborated with customers to understand and implement findings within their organizations. Heavily researched industry trends and provided competitive analysis. Managed research vendors to ensure projects were completed on time and within budget.</p>
    </article>
    <article class="job">
      <div class="job-org">Coastal State University Survey Research Center.<span class="job-role small">Field Director, Program Manager, and Ethnographer</span></div>
      <div class="job-dates">2003 - 2007</div>
      <p><span class="sub">Field Director</span> (2007) Oversaw the hiring, training, scheduling, and general management of 200+ phone interviewers. Managed small teams of employees responsible for the construction of research designs emphasizing validity, accuracy, and precision.</p>
      <p><span class="sub">Program Manager/Graduate Research Assistant</span> (2001 to 2006) Directed full survey project lifecycle for research center under the Center for Regional Economic Studies. Spearheaded all efforts regarding telephone survey questionnaire development, QuestForm programming, sample management, data cleaning, and analysis and report production.</p>
      <p><span class="sub">Ethnographer, Social Network Projects</span> (2004) Collected egocentric network data on Mexican migrants in Northwestern Kansas in relation to National Science Alliance grant under Dr. Alan Whitford. Formulated models of acculturation and enculturation based on ethnographic field work and network data.</p>
    </article>
  </section>

  <h2 class="side-bar contact-head">Contact Details</h2>
  <address class="contact">
    <p>4120 Oak Ridge Road,<br>Fairhaven, FL<br>32900</p>
    <p>(555) 014-2287</p>
    <p>daniel@brightpathresearch.com</p>
  </address>

  <h2 class="side-bar skills-head">Skills</h2>
  <ul class="skills">
    <li>- Research Design</li>
    <li>- Data Collection</li>
    <li>- Research</li>
    <li>- Analysis</li>
    <li>- Strategic Planning</li>
    <li>- Interviews</li>
    <li>- Management</li>
    <li>- Testing</li>
    <li>- Focus Groups</li>
    <li>- Anthropology</li>
    <li>- StatCore</li>
    <li>- DataLens</li>
    <li>- QuestForm</li>
  </ul>
  <div class="side-foot"></div>
</main>
</body>
</html>
```